Need webdesign for service company that provides Car hiring service and transit service

We need a web design for a company that provides airport transit services and transport services including Limo, Corporate cars, Disability transit, Family transit service. We need is a simple and professional design.

Below is site which we like and also offer the same service http://www.ridelyntrek.com.au/

Reason: Waiting for the Feedback from multiple stakeholders. Need the time to select and approve the design

Target Market(s)

Tourism, Travel

Industry/Entity Type

Airport

Number of Pages Required

3 page

Font styles to use
Decorative
Script

Requirements
Must have
• Simple and Professional, Site we like http://www.ridelyntrek.com.au/ and also need to mobile friendly
Should not have
• Shouldn't have too many images

```html
<!DOCTYPE html>
<html lang="en">
<head>
<meta charset="utf-8">
<title>RidePoint – Car Hire &amp; Transit</title>
<link href="https://fonts.googleapis.com/css2?family=Roboto:wght@300;400;500;700&family=Roboto+Condensed:wght@400;700&display=swap" rel="stylesheet">
<style>
:root{
  --ink:#1d1d1d;
  --dark:#1b1b1b;
  --darker:#111111;
  --panel:#2a2a2a;
  --mid:#555555;
  --muted:#777777;
  --line:#cfcfcf;
  --light:#ececec;
  --paper:#ffffff;
  --accent:#3a3a3a;
}
*{box-sizing:border-box;margin:0;padding:0}
html,body{width:1200px;height:2768px;overflow:hidden}
body{font-family:"Roboto",Arial,sans-serif;color:var(--ink);background:var(--paper)}
.section{position:relative;width:1200px;overflow:hidden}
.btn{display:inline-block;border:2px solid var(--ink);padding:9px 18px;font:500 13px "Roboto",sans-serif;letter-spacing:1px;color:var(--ink);text-transform:uppercase;background:var(--paper)}
.btn-light{border-color:#fff;color:#fff;background:transparent}

/* header */
.topbar{height:100px;background:var(--dark);display:flex;align-items:center;padding:0 112px;justify-content:space-between}
.brand{display:flex;align-items:center;gap:12px;color:#fff;font:700 34px "Roboto",sans-serif;letter-spacing:1px}
.brand-mark{width:40px;height:40px;border:2px solid #fff}
.top-tools{display:flex;gap:10px;align-items:center}
.search{width:240px;height:34px;border:1px solid #555;background:#0f0f0f;color:#999;font-size:12px;display:flex;align-items:center;justify-content:space-between;padding:0 12px}
.login{height:34px;border:1px solid #fff;color:#fff;font-size:12px;display:flex;align-items:center;gap:6px;padding:0 14px;letter-spacing:1px}
.nav{height:40px;background:var(--darker);display:flex;align-items:center;padding:0 112px;gap:28px}
.nav a{color:#bbb;font:500 13px "Roboto",sans-serif;text-decoration:none;text-transform:uppercase}
.nav a.active{color:#fff;border-bottom:2px solid #fff;padding-bottom:4px}

/* hero */
.hero{height:360px;background:linear-gradient(135deg,#f2f2f2 0%,#dcdcdc 45%,#ececec 70%,#d4d4d4 100%)}
.hero-copy{position:absolute;left:112px;top:60px;width:330px}
.hero-copy h1{font:700 38px "Roboto Condensed",sans-serif;text-transform:uppercase;line-height:1.1}
.hero-copy h2{font:400 17px "Roboto",sans-serif;margin:8px 0 16px;color:var(--mid)}
.hero-copy p{font-size:13px;line-height:1.6;color:var(--mid);margin-bottom:20px}
.hero-car{position:absolute;left:470px;top:40px;width:560px;height:290px;border-radius:120px 160px 40px 40px;background:radial-gradient(ellipse at 50% 40%,#4a4a4a,#111 75%)}

/* quote */
.quote{height:500px;background:var(--paper);padding-top:70px}
.section-title{text-align:center;font:300 36px "Roboto",sans-serif;text-transform:uppercase;letter-spacing:1px}
.section-title b{font-weight:700}
.title-rule{width:300px;height:1px;background:var(--line);margin:14px auto 0}
.quote-form{position:absolute;left:112px;top:190px;width:976px;display:grid;grid-template-columns:repeat(4,1fr);column-gap:28px;row-gap:30px}
.field label{display:block;font:500 15px "Roboto",sans-serif;margin-bottom:8px}
.input{height:38px;border:1px solid var(--line);display:flex;align-items:center;gap:10px;padding:0 12px;font-size:13px;color:var(--muted)}
.field.wide{grid-column:span 2}
.quote .btn{position:absolute;left:50%;transform:translateX(-50%);top:410px}

/* about */
.about{height:390px;background:linear-gradient(180deg,#efefef,#d2d2d2 55%,#bdbdbd)}
.about .section-title{padding-top:100px}
.about p{width:920px;margin:30px auto 0;text-align:center;font:500 14px/1.7 "Roboto",sans-serif;color:var(--ink)}

/* tourism */
.tourism{height:410px;background:var(--paper)}
.tourism-photo{position:absolute;left:112px;top:60px;width:450px;height:290px;background:linear-gradient(135deg,#a98a6b,#5e4a3a 50%,#c7b7a3)}
.tourism-copy{position:absolute;left:610px;top:70px;width:460px}
.tourism-copy h2{font:300 32px "Roboto",sans-serif;text-transform:uppercase;line-height:1.2}
.tourism-copy .title-rule{margin:14px 0 20px;width:380px}
.tourism-copy p{font-size:13px;line-height:1.7;color:var(--mid);margin-bottom:22px}

/* join */
.join{height:380px;display:flex}
.join-card{width:600px;height:380px;text-align:center;color:#fff;padding-top:60px}
.join-member{background:var(--dark)}
.join-driver{background:var(--panel)}
.join-card h2{font:400 30px "Roboto",sans-serif;text-transform:uppercase;letter-spacing:1px;margin:16px 0 18px}
.join-card p{width:400px;margin:0 auto 24px;font-size:13px;line-height:1.6;color:#cfcfcf}

/* testimonial */
.testimonial{height:380px;background:linear-gradient(160deg,#fafafa,#e4e4e4)}
.testimonial .section-title{padding-top:60px;font-size:30px}
.review{position:absolute;left:112px;top:170px;width:976px;height:160px;background:var(--paper);border:1px solid #e2e2e2;padding:30px 60px 0 180px}
.avatar{position:absolute;left:50px;top:30px;width:100px;height:100px;border-radius:50%;background:radial-gradient(circle at 50% 40%,#c9a88a,#6d5646)}
.review p{font-size:13px;line-height:1.7;color:var(--mid)}
.review .who{margin-top:12px;font:700 13px "Roboto",sans-serif;color:var(--ink)}
.review .who span{font-weight:400;color:var(--muted);margin-left:10px}
.qmark{position:absolute;font:700 40px Georgia,serif;color:var(--ink)}

/* footer */
.footer{height:208px;background:var(--paper);border-top:1px solid #e6e6e6;text-align:center;padding-top:50px}
.footer .brand{color:var(--ink);justify-content:center}
.footer .brand-mark{border-color:var(--ink)}
.footer-rule{width:620px;height:1px;background:var(--line);margin:30px auto 16px}
.footer small{font-size:12px;color:var(--mid)}
</style>
</head>
<body>

<header class="section">
  <div class="topbar">
    <div class="brand"><span class="brand-mark"></span>RIDEPOINT</div>
    <div class="top-tools">
      <div class="search">Search
        <svg width="14" height="14" viewBox="0 0 14 14"><circle cx="6" cy="6" r="4.5" fill="none" stroke="#ccc" stroke-width="1.5"/><line x1="9.5" y1="9.5" x2="13" y2="13" stroke="#ccc" stroke-width="1.5"/></svg>
      </div>
      <div class="login">
        <svg width="12" height="12" viewBox="0 0 12 12"><rect x="1" y="1" width="10" height="10" fill="none" stroke="#fff"/><path d="M3 6h5M6 4l2 2-2 2" fill="none" stroke="#fff"/></svg>LOGIN
      </div>
    </div>
  </div>
  <nav class="nav">
    <a class="active">Home</a><a>About us</a><a>Our company</a><a>Our people</a><a>Fleet &amp; Drivers</a><a>Testimonials</a><a>News &amp; Events</a><a>FAQ</a><a>Contact us</a>
  </nav>
</header>

<section class="section hero">
  <div class="hero-copy">
    <h1>Great car hire deals</h1>
    <h2>Find best rental car</h2>
    <p>Our fleet is ready whenever you are. Choose from sedans, limousines and family vans, all cleaned, serviced and driven by friendly local professionals who know every route.</p>
    <span class="btn">Book now</span>
  </div>
  <div class="hero-car" role="img" aria-label="Black luxury sedan shown in side view"></div>
</section>

<section class="section quote">
  <h2 class="section-title">Instant <b>Quote</b></h2>
  <div class="title-rule"></div>
  <div class="quote-form">
    <div class="field"><label>Pick up Date</label><div class="input">
      <svg width="14" height="14" viewBox="0 0 14 14"><rect x="1" y="2" width="12" height="11" fill="none" stroke="#777"/><line x1="1" y1="5" x2="13" y2="5" stroke="#777"/></svg>07/02/2017</div></div>
    <div class="field"><label>Pick up Time</label><div class="input">
      <svg width="14" height="14" viewBox="0 0 14 14"><circle cx="7" cy="7" r="6" fill="none" stroke="#777"/><path d="M7 3v4h3" fill="none" stroke="#777"/></svg>09:00 AM</div></div>
    <div class="field"><label>Return Date</label><div class="input">
      <svg width="14" height="14" viewBox="0 0 14 14"><rect x="1" y="2" width="12" height="11" fill="none" stroke="#777"/><line x1="1" y1="5" x2="13" y2="5" stroke="#777"/></svg>07/02/2017</div></div>
    <div class="field"><label>Return Time</label><div class="input">
      <svg width="14" height="14" viewBox="0 0 14 14"><circle cx="7" cy="7" r="6" fill="none" stroke="#777"/><path d="M7 3v4h3" fill="none" stroke="#777"/></svg>09:00 AM</div></div>
    <div class="field wide"><label>Pick up Location</label><div class="input">
      <svg width="12" height="14" viewBox="0 0 12 14"><path d="M6 13C2 8 1 6.5 1 5a5 5 0 0 1 10 0c0 1.5-1 3-5 8z" fill="none" stroke="#777"/><circle cx="6" cy="5" r="1.6" fill="#777"/></svg>Kingston</div></div>
    <div class="field wide"><label>Return Location</label><div class="input">
      <svg width="12" height="14" viewBox="0 0 12 14"><path d="M6 13C2 8 1 6.5 1 5a5 5 0 0 1 10 0c0 1.5-1 3-5 8z" fill="none" stroke="#777"/><circle cx="6" cy="5" r="1.6" fill="#777"/></svg>Kingston</div></div>
  </div>
  <span class="btn">Estimate Fare</span>
</section>

<section class="section about" role="img" aria-label="Faded city skyline behind the about text">
  <h2 class="section-title">About <b>RidePoint</b></h2>
  <p>For more than twenty years we have moved travellers across the region with care. From early airport runs to late corporate dinners, our drivers arrive on time, help with luggage and take the calmest route. We offer limousines, executive cars, accessible vehicles for passengers with disability and roomy vans for families, so every trip fits the people taking it. Booking is quick, prices are clear and our support team is available around the clock.</p>
</section>

<section class="section tourism">
  <div class="tourism-photo" role="img" aria-label="Smiling couple seated in the back of a hire car"></div>
  <div class="tourism-copy">
    <h2>Book us for tourism or travel</h2>
    <div class="title-rule"></div>
    <p>Planning a holiday or a day of sightseeing? Our drivers know the best spots, the quiet roads and the easiest places to stop. Relax in comfort while we handle the traffic, parking and timing, and enjoy every part of your journey without the stress of driving.</p>
    <span class="btn">Book now</span>
  </div>
</section>

<section class="section join">
  <div class="join-card join-member">
    <svg width="60" height="50" viewBox="0 0 60 50"><circle cx="24" cy="14" r="10" fill="#fff"/><path d="M4 48c0-13 9-20 20-20s20 7 20 20z" fill="#fff"/><path d="M48 10v16M40 18h16" stroke="#fff" stroke-width="4"/></svg>
    <h2>Become a member</h2>
    <p>Members enjoy priority bookings, saved trip details and special rates on airport transfers. Sign up in a few minutes and start travelling smarter with us.</p>
    <span class="btn btn-light">Become a member</span>
  </div>
  <div class="join-card join-driver">
    <svg width="60" height="50" viewBox="0 0 60 50"><circle cx="24" cy="14" r="10" fill="#fff"/><path d="M4 48c0-13 9-20 20-20s20 7 20 20z" fill="#fff"/><circle cx="47" cy="30" r="10" fill="none" stroke="#fff" stroke-width="3"/><path d="M47 24v6h5" fill="none" stroke="#fff" stroke-width="2.5"/></svg>
    <h2>Become a driver</h2>
    <p>Set your own hours and drive with a team that values safety and service. We support our drivers with steady work, fair pay and a modern fleet.</p>
    <span class="btn btn-light">Become a driver</span>
  </div>
</section>

<section class="section testimonial">
  <h2 class="section-title">Our <b>Testimonial</b></h2>
  <div class="title-rule"></div>
  <div class="review">
    <div class="avatar" role="img" aria-label="Customer portrait"></div>
    <span class="qmark" style="left:160px;top:6px">&ldquo;</span>
    <p>The driver met us right at arrivals, helped with every bag and had us at the hotel in no time. The car was spotless and the booking was simple. We have used the service three times since and each trip has been just as smooth. Highly recommended for families and business travellers alike.</p>
    <div class="who">Martin Hale Corbett<span>Businessman</span></div>
    <span class="qmark" style="right:24px;bottom:-10px">&rdquo;</span>
  </div>
</section>

<footer class="section footer">
  <div class="brand"><span class="brand-mark"></span>RIDEPOINT</div>
  <div class="footer-rule"></div>
  <small>RidePoint &copy; 2017 &nbsp;|&nbsp; All Rights Reserved &nbsp;|&nbsp; Privacy Policy &nbsp;|&nbsp; Terms &amp; Conditions</small>
</footer>

</body>
</html>
```